R7 Web Design Project

New company website for Intel cyber security company.

Style should be cool, but remain appropriate for very serious subject matter and audience.

Target Market(s)

Target audience is government and the military

Navigation needs to include:
- About Us
- Services
- Careers
- Contact Us
- Contracts

As well as 2 feature areas - use "Technology Integration" and "Case Study" as the supporting headlines.

Industry/Entity Type

Security

Font styles to use
Sans Serif

Colors

Designer to choose colors to be used in the design.

Requirements
Must have
• Mountain imagery and theme.

Use logo attached.

New Tagline - "Defending the Domain"
Nice to have
• Supporting imagery could include photos representative of security - avoid cliches.
Should not have
• Needs to be serious not frivolous

```html
<!DOCTYPE html>
<html lang="en">
<head>
<meta charset="utf-8">
<title>R7 Group — Defending the Domain</title>
<link rel="stylesheet" href="https://fonts.googleapis.com/css2?family=Bitter:ital,wght@0,400;0,500;0,700;1,400;1,500&family=Lato:ital,wght@0,400;0,700;1,400&display=swap">
<style>
  :root {
    --navy: #1f3379;
    --navy-deep: #1b2d6b;
    --ink: #333333;
    --charcoal: #2f2f2f;
    --rule: #b9c0cc;
    --panel: #ededed;
    --white: #ffffff;
  }
  * { box-sizing: border-box; margin: 0; padding: 0; }
  html, body { width: 992px; height: 1200px; overflow: hidden; }
  body { position: relative; background: var(--white); font-family: "Lato", sans-serif; color: var(--ink); }

  /* Header */
  .site-header { position: absolute; left: 0; top: 0; width: 992px; height: 110px; background: var(--white); border-top: 2px solid var(--navy-deep); border-bottom: 3px solid var(--charcoal); }
  .brand { position: absolute; left: 108px; top: 24px; display: flex; align-items: center; gap: 14px; }
  .brand-mark { width: 62px; height: 62px; background: var(--navy); }
  .brand-name { font-family: "Bitter", serif; font-weight: 400; font-size: 35px; color: var(--navy); letter-spacing: 0.3px; }
  .tagline { position: absolute; right: 272px; top: 22px; font-family: "Lato", sans-serif; font-size: 22px; color: var(--charcoal); letter-spacing: 0.3px; white-space: nowrap; }
  .phone { position: absolute; left: 736px; top: 22px; display: flex; align-items: center; gap: 8px; font-style: italic; font-size: 19px; color: #555; }
  .main-nav { position: absolute; right: 108px; top: 79px; display: flex; gap: 18px; }
  .main-nav a { font-family: "Bitter", serif; font-weight: 700; font-size: 12px; letter-spacing: 0.5px; color: var(--charcoal); text-decoration: none; position: relative; }
  .main-nav a.active { color: var(--navy); }
  .main-nav a.active::after { content: ""; position: absolute; left: -2px; right: -2px; top: 18px; height: 10px; background: var(--white); }

  /* Hero */
  .hero { position: absolute; left: 0; top: 110px; width: 992px; height: 400px;
    background: linear-gradient(90deg, #e7a03a 0%, #d9a774 14%, #9cc9cb 34%, #5b8ea0 50%, #8fd5d7 70%, #7fd9de 100%); }
  .hero-caption { position: absolute; left: 243px; top: 166px; width: 504px; height: 69px; background: rgba(60,60,60,0.6); display: flex; align-items: center; justify-content: center; text-align: center; font-family: "Bitter", serif; font-weight: 700; font-size: 19px; line-height: 26px; color: var(--white); text-shadow: 1px 1px 2px rgba(0,0,0,0.5); }
  .hero-arrow { position: absolute; top: 158px; width: 44px; height: 84px; background: rgba(255,255,255,0.7); display: flex; align-items: center; justify-content: center; }
  .hero-arrow.prev { left: 58px; border-radius: 0 42px 42px 0; }
  .hero-arrow.next { left: 888px; border-radius: 42px 0 0 42px; }

  /* Audience cards */
  .audience { position: absolute; top: 444px; width: 194px; height: 117px; background: #f4f4f4; border-radius: 4px; box-shadow: 0 2px 6px rgba(0,0,0,0.35); padding: 6px; text-decoration: none; }
  .audience.government { left: 298px; }
  .audience.military { left: 507px; width: 188px; }
  .audience-art { height: 62px; margin: 0 auto; width: 90px; border-radius: 2px; }
  .government .audience-art { background: var(--navy); }
  .military .audience-art { background: #3a3a3a; width: 96px; }
  .audience-label { position: absolute; left: 4px; right: 4px; bottom: 4px; height: 43px; display: flex; align-items: center; justify-content: center; font-family: "Bitter", serif; font-weight: 500; font-size: 20px; letter-spacing: 0.8px; color: var(--white); border-radius: 2px; }
  .government .audience-label { background: var(--navy); }
  .military .audience-label { background: var(--charcoal); }

  /* Content backdrop */
  .backdrop { position: absolute; left: 0; top: 510px; width: 992px; height: 630px;
    background: linear-gradient(180deg, #e2e9f2 0%, #c9d4e3 30%, #dde4ee 60%, #cfd8e5 100%); }

  .welcome { position: absolute; left: 106px; top: 604px; width: 780px; text-align: center; }
  .welcome h1 { font-family: "Bitter", serif; font-weight: 400; font-size: 26px; color: var(--charcoal); padding-bottom: 1px; margin: 0 2px; border-bottom: 1px solid var(--rule); }
  .welcome h1 span { color: var(--navy); }
  .welcome p { margin-top: 11px; font-style: italic; font-size: 12px; line-height: 18.6px; color: var(--ink); letter-spacing: -0.05px; }
  .read-more { display: inline-block; margin-top: 8px; font-family: "Bitter", serif; font-weight: 700; font-size: 11px; letter-spacing: 0.5px; color: var(--navy); text-decoration: underline; }

  .feature { position: absolute; top: 786px; width: 372px; }
  .feature.tech { left: 108px; }
  .feature.cases { left: 510px; }
  .feature h2 { font-family: "Bitter", serif; font-weight: 400; font-size: 19px; color: var(--charcoal); height: 33px; border-bottom: 1px solid var(--rule); position: relative; }
  .feature h2 svg { position: absolute; right: 4px; bottom: 0; }
  .feature-panel { margin-top: 10px; height: 270px; background: var(--panel); border: 1px solid #d3d3d3; border-radius: 4px; box-shadow: 0 4px 10px rgba(0,0,0,0.25); }
  .feature-pager { display: flex; justify-content: center; gap: 8px; margin-top: 7px; }

  .article { margin: 0 27px; padding: 20px 0 8px; }
  .article + .article { border-top: 1px solid #dcdcdc; padding-top: 10px; }
  .article h3 { font-family: "Bitter", serif; font-style: italic; font-weight: 500; font-size: 13.5px; color: var(--navy); margin-bottom: 10px; }
  .article p { font-size: 11px; line-height: 15.3px; color: var(--ink); letter-spacing: 0; word-spacing: -0.3px; }

  .case { display: flex; gap: 20px; margin: 0 24px; padding: 18px 0 16px 4px; height: 90px; }
  .case + .case { border-top: 1px solid #dcdcdc; padding-top: 18px; }
  .case svg { flex-shrink: 0; }
  .case time { display: block; font-weight: 700; font-size: 11.5px; color: var(--navy); margin-top: 2px; margin-bottom: 6px; }
  .case p { font-size: 11.5px; line-height: 16px; color: var(--ink); }

  /* Footer */
  .site-footer { position: absolute; left: 0; top: 1140px; width: 992px; height: 60px; background: var(--navy); color: var(--white); font-family: "Bitter", serif; font-size: 11.5px; letter-spacing: 0.3px; }
  .footer-nav { position: absolute; left: 109px; top: 24px; }
  .footer-nav a { color: var(--white); text-decoration: none; }
  .copyright { position: absolute; right: 111px; top: 24px; }
</style>
</head>
<body>
  <header class="site-header">
    <div class="brand"><span class="brand-mark"></span><span class="brand-name">R7 GROUP</span></div>
    <div class="tagline">DEFENDING THE DOMAIN</div>
    <div class="phone">
      <svg width="22" height="22" viewBox="0 0 22 22"><circle cx="11" cy="11" r="10" fill="none" stroke="#2f2f2f" stroke-width="2"/><path d="M7.5 6.5c1-1 1.8-.6 2.3.3l.7 1.4c.3.6 0 1.1-.5 1.5l-.5.4c.5 1.3 1.6 2.4 2.9 2.9l.4-.5c.4-.5.9-.8 1.5-.5l1.4.7c.9.5 1.3 1.300.3 2.300-1.2 1.2-3.300.8-5.500-1.400S6.300 7.700 7.500 6.500z" fill="#2f2f2f"/></svg>
      555 014 2290
    </div>
    <nav class="main-nav">
      <a class="active" href="#">HOME</a>
      <a href="#">ABOUT US</a>
      <a href="#">SERVICES</a>
      <a href="#">CAREERS</a>
      <a href="#">CONTACT US</a>
      <a href="#">CONTRACTS</a>
    </nav>
  </header>

  <section class="hero" role="img" aria-label="Photo of a hand touching a glowing security interface with a padlock and digital icons">
    <div class="hero-arrow prev"><svg width="16" height="26" viewBox="0 0 16 26"><path d="M13 3L4 13l9 10" fill="none" stroke="#2f2f2f" stroke-width="4"/></svg></div>
    <div class="hero-caption">Our Reputation Is Built On Our Professionalism,<br>Service &amp; Commitment To Excellence</div>
    <div class="hero-arrow next"><svg width="16" height="26" viewBox="0 0 16 26"><path d="M3 3l9 10-9 10" fill="none" stroke="#2f2f2f" stroke-width="4"/></svg></div>
  </section>

  <div class="backdrop" role="img" aria-label="Faded photo of snow-covered mountain peaks"></div>

  <a class="audience government" href="#">
    <div class="audience-art" role="img" aria-label="Government building icon"></div>
    <span class="audience-label">GOVERNMENT</span>
  </a>
  <a class="audience military" href="#">
    <div class="audience-art" role="img" aria-label="Silhouettes of soldiers"></div>
    <span class="audience-label">MILITARY</span>
  </a>

  <section class="welcome">
    <h1>WELCOME to <span>R7 GROUP</span></h1>
    <p>Lorem ipsum dolor sit amet, consectetuer adipiscing elit, sed diam nonummy nibh euismod tincidunt ut laoreet dolore magna aliquam erat volutpat. Ut wisi enim ad minim veniam, quis nostrud exerci tation ullamcorper suscipit lobortis nisl ut aliquip ex ea commodo consequat. Duis autem vel eum iriure dolor in hendrerit in vulputate velit esse molestieconsequat, vel illum dolore eu feugiat nulla facili. Lorem ipsum dolor sit amet, consectetuer adipiscing elit, sed diam nonummy nibh euismod tincidunt ut laoreet dolore magna aliquam erat volutpat. Ut wisi enim ad minim veniam, quis nostrud exerci tation ullamcorper suscipit lobortis nisl ut aliquip ex ea commodo consequat.</p>
    <a class="read-more" href="#">READ MORE</a>
  </section>

  <section class="feature tech">
    <h2>Technology Integration<svg width="16" height="16" viewBox="0 0 16 16"><path d="M3 15L11 3M8 15L16 3" stroke="#1f3379" stroke-width="2"/></svg></h2>
    <div class="feature-panel">
      <article class="article">
        <h3>Lorem ipsum dolor sit amet, consectetuer adipisci</h3>
        <p>Lorem ipsum dolor sit amet, consectetuer adipiscing elit, sed diam nonuod tincidunt ut laoreet dolore magna aliquam erat volutpat. Ut wisi enimm, quis nostrud exerci tation ullamcorper suscipit lobortis nisl ut Lorem ipsum dolor sit amet, consectetuer adipiscing elit, sed diam nonuod tincidunt</p>
      </article>
      <article class="article">
        <h3>Lorem ipsum dolor sit amet, consectetuer adipisci</h3>
        <p>Lorem ipsum dolor sit amet, consectetuer adipiscing elit, sed diam nonuod tincidunt ut laoreet dolore magna aliquam erat volutpat. Ut wisi enimm, quis nostrud exerci tation ullamcorper suscipit lobortis nisl ut Lorem ipsum dolor sit amet, consectetuer adipiscing elit, sed diam nonuod tincidunt</p>
      </article>
    </div>
    <div class="feature-pager">
      <svg width="16" height="16" viewBox="0 0 16 16"><circle cx="8" cy="8" r="7" fill="none" stroke="#555" stroke-width="1.2"/><path d="M12 8H4.5M7.5 5L4.5 8l3 3" fill="none" stroke="#555" stroke-width="1.2"/></svg>
      <svg width="16" height="16" viewBox="0 0 16 16"><circle cx="8" cy="8" r="7" fill="none" stroke="#555" stroke-width="1.2"/><path d="M4 8h7.5M8.5 5l3 3-3 3" fill="none" stroke="#555" stroke-width="1.2"/></svg>
    </div>
  </section>

  <section class="feature cases">
    <h2>Case Study<svg width="16" height="16" viewBox="0 0 16 16"><path d="M3 15L11 3M8 15L16 3" stroke="#1f3379" stroke-width="2"/></svg></h2>
    <div class="feature-panel">
      <article class="case">
        <svg width="36" height="38" viewBox="0 0 36 38"><rect x="2" y="5" width="32" height="31" rx="3" fill="none" stroke="#111" stroke-width="3"/><rect x="2" y="5" width="32" height="8" fill="#111"/><rect x="9" y="1" width="4" height="8" rx="1" fill="#111"/><rect x="23" y="1" width="4" height="8" rx="1" fill="#111"/><g fill="#111"><rect x="7" y="17" width="5" height="4"/><rect x="14" y="17" width="5" height="4"/><rect x="21" y="17" width="5" height="4"/><rect x="7" y="23" width="5" height="4"/><rect x="14" y="23" width="5" height="4"/><rect x="21" y="23" width="5" height="4"/><rect x="7" y="29" width="5" height="3"/><rect x="14" y="29" width="5" height="3"/></g></svg>
        <div><time>26-DEC-2014</time><p>Lorem ipsum dolor sit amet, consectetuer adipiscil ng elit, sed diam nonummy nibh...</p></div>
      </article>
      <article class="case">
        <svg width="36" height="38" viewBox="0 0 36 38"><rect x="2" y="5" width="32" height="31" rx="3" fill="none" stroke="#111" stroke-width="3"/><rect x="2" y="5" width="32" height="8" fill="#111"/><rect x="9" y="1" width="4" height="8" rx="1" fill="#111"/><rect x="23" y="1" width="4" height="8" rx="1" fill="#111"/><g fill="#111"><rect x="7" y="17" width="5" height="4"/><rect x="14" y="17" width="5" height="4"/><rect x="21" y="17" width="5" height="4"/><rect x="7" y="23" width="5" height="4"/><rect x="14" y="23" width="5" height="4"/><rect x="21" y="23" width="5" height="4"/><rect x="7" y="29" width="5" height="3"/><rect x="14" y="29" width="5" height="3"/></g></svg>
        <div><time>27-DEC-2014</time><p>Lorem ipsum dolor sit amet, consectetuer adipiscil ng elit, sed diam nonummy nibh...</p></div>
      </article>
      <article class="case">
        <svg width="36" height="38" viewBox="0 0 36 38"><rect x="2" y="5" width="32" height="31" rx="3" fill="none" stroke="#111" stroke-width="3"/><rect x="2" y="5" width="32" height="8" fill="#111"/><rect x="9" y="1" width="4" height="8" rx="1" fill="#111"/><rect x="23" y="1" width="4" height="8" rx="1" fill="#111"/><g fill="#111"><rect x="7" y="17" width="5" height="4"/><rect x="14" y="17" width="5" height="4"/><rect x="21" y="17" width="5" height="4"/><rect x="7" y="23" width="5" height="4"/><rect x="14" y="23" width="5" height="4"/><rect x="21" y="23" width="5" height="4"/><rect x="7" y="29" width="5" height="3"/><rect x="14" y="29" width="5" height="3"/></g></svg>
        <div><time>28-DEC-2014</time><p>Lorem ipsum dolor sit amet, consectetuer adipiscil ng elit, sed diam nonummy nibh...</p></div>
      </article>
    </div>
    <div class="feature-pager">
      <svg width="16" height="16" viewBox="0 0 16 16"><circle cx="8" cy="8" r="7" fill="none" stroke="#555" stroke-width="1.2"/><path d="M12 8H4.5M7.5 5L4.5 8l3 3" fill="none" stroke="#555" stroke-width="1.2"/></svg>
      <svg width="16" height="16" viewBox="0 0 16 16"><circle cx="8" cy="8" r="7" fill="none" stroke="#555" stroke-width="1.2"/><path d="M4 8h7.5M8.5 5l3 3-3 3" fill="none" stroke="#555" stroke-width="1.2"/></svg>
    </div>
  </section>

  <footer class="site-footer">
    <nav class="footer-nav"><a href="#">HOME</a> &nbsp;/&nbsp; <a href="#">ABOUT US</a> &nbsp;/&nbsp; <a href="#">SERVICES</a> &nbsp;/&nbsp; <a href="#">CAREERS</a> &nbsp;/&nbsp; <a href="#">CONTACT US</a> &nbsp;/&nbsp; <a href="#">CONTRACTS</a></nav>
    <div class="copyright">COPYRIGHT 2014 © R7 Group. All Rights Reserved.</div>
  </footer>
</body>
</html>
```